its a towing company , its called kwm towing and transport. kwm stands for kept with merit. on the card looking for colors mainly red with gray and black and white. what the company do. local and long distances ,buy junk cars , snow plow available .tire change ,jumpstart ,and fuel delivery find us on pagewell . kwmtowing@mailora.com. fax no#555-210-4867 phone no#555-386-2074

something that defines kept with merit

Decorative

ef444b
1b1b1b
9d9d9d
ffffff

• pics of chains or flatbed varn in red
• no cartoons

```html
<!DOCTYPE html>
<html lang="en">
<head>
<meta charset="utf-8">
<title>KWM Towing and Transport – Business Card</title>
<link href="https://fonts.googleapis.com/css2?family=Lato:wght@400;700;900&display=swap" rel="stylesheet">
<style>
  :root {
    --red: #ef444b;
    --ink: #1b1b1b;
    --gray: #9d9d9d;
    --white: #ffffff;
    --backdrop: #e6e6e6;
  }
  * { box-sizing: border-box; margin: 0; padding: 0; }
  html, body { width: 1200px; height: 900px; overflow: hidden; }
  body {
    background: var(--backdrop);
    font-family: "Lato", Arial, sans-serif;
    color: var(--ink);
    display: flex;
    flex-direction: column;
    align-items: center;
    justify-content: center;
    gap: 36px;
  }
  .card {
    position: relative;
    width: 700px;
    height: 400px;
    overflow: hidden;
    box-shadow: 0 6px 18px rgba(0,0,0,0.18);
  }

  /* ---------- Back side ---------- */
  .card-back { background: var(--gray); }
  .truck-photo {
    position: absolute; inset: 0;
    background: linear-gradient(160deg, #b9b7b2 0%, #8e8f93 35%, #a0343a 55%, #c9c7c4 78%, #7b7c80 100%);
  }
  .photo-veil { position: absolute; inset: 0; background: rgba(157,157,157,0.45); }
  .back-brand {
    position: absolute;
    top: 118px; left: 0; right: 0;
    text-align: center;
    color: var(--white);
    font-weight: 900;
    line-height: 1;
  }
  .back-brand .brand-initials { display: block; font-size: 84px; letter-spacing: 2px; }
  .back-brand .brand-rest { display: block; font-size: 40px; margin-top: 4px; }
  .service-band {
    position: absolute;
    left: 0; right: 0; bottom: 36px;
    height: 88px;
    background: var(--red);
    color: var(--white);
    font-weight: 700;
    font-size: 19px;
    display: flex;
    flex-direction: column;
    justify-content: center;
    align-items: center;
    gap: 6px;
    letter-spacing: 0.3px;
  }

  /* ---------- Front side ---------- */
  .card-front { background: var(--white); }
  .front-brand {
    position: absolute;
    top: 44px; left: 150px;
    color: var(--ink);
    font-weight: 900;
    line-height: 1;
  }
  .front-brand .brand-initials { display: block; font-size: 70px; letter-spacing: 2px; padding-left: 60px; }
  .front-brand .brand-rest { display: block; font-size: 36px; margin-top: 2px; }
  .divider {
    position: absolute;
    top: 176px; left: 56px;
    width: 590px; height: 2px;
    background: var(--red);
  }
  .contact-list {
    position: absolute;
    top: 196px; left: 56px;
    list-style: none;
    font-size: 20px;
    line-height: 28px;
  }
  .contact-list li { display: flex; align-items: center; gap: 10px; }
  .contact-list svg { width: 16px; height: 16px; flex: none; }
  .person {
    position: absolute;
    top: 196px; right: 54px;
    text-align: right;
  }
  .person-name {
    color: var(--red);
    font-weight: 700;
    font-size: 30px;
    border-bottom: 2px solid var(--red);
    padding-bottom: 2px;
  }
  .person-role { font-size: 21px; margin-top: 4px; }
  .address {
    position: absolute;
    top: 290px; right: 54px;
    text-align: right;
    font-size: 22px;
    line-height: 28px;
  }
  .edge-bands {
    position: absolute; left: 0; bottom: 0;
    width: 700px; height: 56px;
  }
  .payment-note {
    position: absolute;
    right: 40px; bottom: 14px;
    color: var(--white);
    font-size: 22px;
    letter-spacing: 0.5px;
  }
</style>
</head>
<body>

  <section class="card card-back" aria-label="Card back">
    <div class="truck-photo" role="img" aria-label="Photo of a red flatbed tow truck parked on a road"></div>
    <div class="photo-veil"></div>
    <h1 class="back-brand">
      <span class="brand-initials">KWM</span>
      <span class="brand-rest">Towing and Transport</span>
    </h1>
    <div class="service-band">
      <p>Local and Long distances • Buy junk cars</p>
      <p>Snow plow available • Tire change • Jump start • Fuel delivery</p>
    </div>
  </section>

  <section class="card card-front" aria-label="Card front">
    <h2 class="front-brand">
      <span class="brand-initials">KWM</span>
      <span class="brand-rest">Towing and Transport</span>
    </h2>

    <div class="divider"></div>

    <ul class="contact-list">
      <li>
        <svg viewBox="0 0 16 16" aria-hidden="true"><path fill="#ef444b" d="M3.5 1.5l2.5 0 1 3.5-1.6 1.2a9 9 0 0 0 4.4 4.4l1.2-1.6 3.5 1v2.5c0 .8-.7 1.5-1.5 1.5C6.8 14 2 9.2 2 3c0-.8.7-1.5 1.5-1.5z"/></svg>
        555-386-2074
      </li>
      <li>
        <svg viewBox="0 0 16 16" aria-hidden="true"><path fill="#ef444b" d="M4 1h8v4H4zM1 6h14v6h-3v3H4v-3H1zM5 10v4h6v-4z"/></svg>
        555-210-4867
      </li>
      <li>
        <svg viewBox="0 0 16 16" aria-hidden="true"><path fill="#ef444b" d="M1 3h14v10H1zM2.5 4.2L8 8.6l5.5-4.4z"/></svg>
        kwmtowing@mailora.com
      </li>
      <li>
        <svg viewBox="0 0 16 16" aria-hidden="true"><rect x="1" y="1" width="14" height="14" fill="#ef444b"/></svg>
        /kwmtowing
      </li>
    </ul>

    <div class="person">
      <p class="person-name">Mara Kellan</p>
      <p class="person-role">Manager</p>
    </div>

    <address class="address" style="font-style:normal">
      4100 Elm Crest Road<br>Harlow TX 75010
    </address>

    <svg class="edge-bands" viewBox="0 0 700 56" aria-hidden="true">
      <polygon points="0,0 300,0 330,56 0,56" fill="#1b1b1b"/>
      <polygon points="300,10 700,10 700,56 326,56" fill="#ef444b"/>
    </svg>
    <p class="payment-note">Credit cards accepted</p>
  </section>

</body>
</html>
```